Wordpress Website Design/Launch for Aerial Drone Company

My company (Skyward Lens Reels) recently obtained NVB 333 clearance to fly drones for commercial use. I am a needing a very simple, but very visual & techy (icons/colors) look and feel website. aerial images of cities, solar farms, agriculture, buildings can be used since our services will focus on providing aerial video & photography for the following sectors:

- Real Estate Videos for commercial, industrial, retail, multi-family and residential, big focus on developers (new construction type projects. (main market)

- Agricultural videos

- Utilities (electrical line inspection, hydro dams, pipelines, sewage plants, solar farms, fracking operations.

- Hospitality (hotels, resorts)

- Retirement Communities

- Hospitals

- CONSERVATION, ENVIRONMENTAL REGULATION AND COMPLIANCE

- Disaster Relief

- Sporting Events / Festivals / Stadiums, Ballparks
- International availability

This It needs to be WordPress
Easily managed by my team on the backend (including: adding copy, uploading and changing videos and pictures)
Must have a blog
No social media now but needs to have plugins added so we can link when ready

The site should appeal to and have a call to action on every page: contact us via phone, contact form, and click the videos (will need to add) .

Right now I see only 5 pages:
Home (background flying videos through cities/over buildings on streets etc ??)
About Us
Services (see above service areas will need icons for each)
Our Work
Contact Us (needs to integrate into Kelvora CRM)
Blog

I am looking for the website to be designed, coded and launch on our hosting server (hostpalm).

Example of a website
http://www.gliderfoxstudios.example

** We do not have a logo so I would like to see whys you can be creative with our name. The website domain is www.skywardlensreels.example.

Target Market(s)

Target market will be:

Real Estate Market (Residential, Commercial, Industrial, developers)
Utilities (Oil companies, electric companies, natural gas companies)
Hospitals
Hotels & Resorts
Farmers (agricultural survey)
Cities & Municipals for aerial surveying/builiding inspections
Blue Harbor Aid / Disaster Relief
Sporting Events / Stadiums - football/Baseball / High School sports

Industry/Entity Type

It Company

Number of Pages Required

5+ page

Requirements
Must have
• Must be very visual
• Include custom icons for the target audience / services
• background video on the home page/ additional pages of flying through cities/streets/ by buildings/ over land / solar farms etc.
• Clean professional look / simple
Nice to have
• I am open to all ideas
• unique logo for our name "Skyward Lens Reels"

```html
<!DOCTYPE html>
<html lang="en">
<head>
<meta charset="utf-8">
<title>Skyward Lens Reels</title>
<link href="https://fonts.googleapis.com/css2?family=Montserrat:wght@400;600;700&family=Open+Sans:wght@400;600&display=swap" rel="stylesheet">
<style>
:root{
  --blue:#2aa7df;
  --blue-dark:#1b8cc0;
  --ink:#2b2f36;
  --dark:#2e3239;
  --darker:#24272d;
  --text:#555b63;
  --muted:#8b9199;
  --light:#f2f3f5;
  --white:#ffffff;
}
*{box-sizing:border-box;margin:0;padding:0}
html,body{width:1200px;height:2668px;overflow:hidden}
body{font-family:"Open Sans",Arial,sans-serif;color:var(--text);background:var(--white);position:relative}
h1,h2,h3,h4,.brand,.nav a,.btn{font-family:"Montserrat",Arial,sans-serif}

/* hero */
.hero{position:absolute;left:0;top:0;width:1200px;height:640px}
.hero-media{position:absolute;inset:0;background:linear-gradient(160deg,#6d8a5a 0%,#8aa276 30%,#a7aeaa 55%,#7c8a93 80%,#596a74 100%)}
.hero-shade{position:absolute;inset:0;background:linear-gradient(180deg,rgba(0,0,0,.35) 0%,rgba(0,0,0,.05) 25%,rgba(0,0,0,.2) 70%,rgba(0,0,0,.3) 100%)}
.topbar{position:absolute;left:0;top:0;width:1200px;height:84px;display:flex;align-items:center;padding:0 70px}
.brand{display:flex;align-items:center;gap:12px;color:var(--white);font-weight:700;font-size:22px;letter-spacing:.5px}
.brand-dot{width:30px;height:30px;border-radius:50%;background:var(--blue)}
.nav{display:flex;gap:30px;margin-left:auto;margin-right:40px}
.nav a{color:var(--white);text-decoration:none;font-size:12px;font-weight:600;letter-spacing:1px;padding-bottom:4px}
.nav a.active{border-bottom:2px solid var(--white)}
.btn{display:inline-flex;align-items:center;justify-content:center;gap:8px;background:var(--blue);color:var(--white);font-size:12px;font-weight:700;letter-spacing:1px;text-transform:uppercase;border:none;border-radius:3px}
.btn-videos{height:44px;padding:0 20px;font-size:13px}
.hero-copy{position:absolute;left:0;top:290px;width:1200px;text-align:center;color:var(--white)}
.hero-copy .eyebrow{font-family:"Montserrat",sans-serif;font-size:30px;font-weight:600}
.hero-copy h1{font-size:46px;font-weight:700;margin-top:4px;letter-spacing:1px}
.hero-copy p{font-size:14px;line-height:1.6;width:560px;margin:14px auto 0;opacity:.95}

/* services */
.services{position:absolute;left:0;top:640px;width:1200px;height:488px;background:var(--white)}
.section-title{text-align:center;font-size:28px;font-weight:700;color:var(--ink);padding-top:50px}
.title-rule{width:60px;height:3px;background:var(--blue);margin:14px auto 0}
.service-grid{position:absolute;left:225px;top:155px;width:750px;display:grid;grid-template-columns:repeat(5,150px);row-gap:34px}
.service{text-align:center}
.service svg{width:62px;height:62px;display:block;margin:0 auto}
.service span{display:block;margin-top:10px;font-size:13px;font-weight:600;color:var(--ink);line-height:1.3;min-height:34px}

/* videos */
.videos{position:absolute;left:0;top:1128px;width:1200px;height:552px;background:var(--dark)}
.video-row{position:absolute;left:70px;top:48px;width:1060px;display:flex;gap:35px}
.video-card{width:330px}
.video-thumb{position:relative;height:200px;border-radius:2px;overflow:hidden}
.thumb-city{background:linear-gradient(150deg,#6b7b86,#98a3a6 50%,#5d6b5a)}
.thumb-farm{background:linear-gradient(150deg,#7e9a6a,#a5b68a 50%,#6c7f5b)}
.thumb-solar{background:linear-gradient(150deg,#9fb0b8,#c5ced3 45%,#6f8a6a)}
.play{position:absolute;left:50%;top:45%;transform:translate(-50%,-50%)}
.controls{position:absolute;left:0;bottom:0;width:100%;height:26px;background:rgba(0,0,0,.55);display:flex;align-items:center;padding:0 10px;gap:10px}
.controls .bar{flex:1;height:4px;background:rgba(255,255,255,.3);border-radius:2px;position:relative}
.controls .bar i{position:absolute;left:0;top:0;height:4px;width:30%;background:var(--blue);border-radius:2px}
.video-card h3{color:var(--white);font-size:20px;font-weight:600;margin-top:26px}
.video-card p{color:#b8bec6;font-size:12px;line-height:1.6;margin-top:10px}
.btn-more{position:absolute;left:540px;top:432px;width:120px;height:38px}

/* blog */
.blog{position:absolute;left:0;top:1680px;width:1200px;height:532px;background:var(--white)}
.blog h2{position:absolute;left:70px;top:40px;font-size:28px;font-weight:700;color:var(--ink)}
.blog-row{position:absolute;left:70px;top:100px;width:1060px;display:flex;gap:35px}
.post{width:330px}
.post-thumb{height:180px;border-radius:2px}
.pt-1{background:linear-gradient(150deg,#7b8f9b,#aab5ba 50%,#6f8260)}
.pt-2{background:linear-gradient(150deg,#6d8460,#9aa98a 50%,#7f8d95)}
.pt-3{background:linear-gradient(150deg,#8d7f62,#a79a77 45%,#5f7352)}
.post h3{font-size:17px;font-weight:600;color:var(--ink);margin-top:22px}
.post .meta{font-size:11px;color:var(--muted);margin-top:6px}
.post p{font-size:12px;line-height:1.6;margin-top:10px}
.post .more{display:block;margin-top:14px;font-size:12px;font-weight:600;color:var(--blue)}

/* newsletter */
.newsletter{position:absolute;left:0;top:2212px;width:1200px;height:78px;background:var(--darker);display:flex;align-items:center;padding:0 70px}
.newsletter h4{color:var(--white);font-size:18px;font-weight:600;margin-left:16px}
.nl-form{display:flex;gap:10px;margin-left:auto}
.field{background:var(--white);border:1px solid #d7dade;border-radius:2px;font-size:12px;color:var(--muted);display:flex;align-items:center;padding:0 12px}
.nl-form .field{width:250px;height:34px}
.btn-sub{height:34px;width:110px}

/* footer */
.footer{position:absolute;left:0;top:2290px;width:1200px;height:378px;background:var(--light)}
.footer h4{font-size:15px;font-weight:700;color:var(--ink);margin-bottom:14px}
.col-links{position:absolute;left:70px;top:36px}
.col-links li{list-style:none;font-size:12px;line-height:2.1}
.col-touch{position:absolute;left:330px;top:36px;width:240px}
.touch-item{display:flex;gap:12px;font-size:12px;line-height:1.5;margin-bottom:16px}
.touch-item svg{flex:none}
.col-form{position:absolute;left:610px;top:36px;width:520px}
.col-form .hint{font-size:11px;color:var(--muted);margin-bottom:10px}
.form-grid{display:grid;grid-template-columns:1fr 1fr;gap:10px}
.form-grid .field{height:32px}
.form-grid .msg{grid-column:1/3;height:80px;align-items:flex-start;padding-top:8px}
.btn-submit{margin-top:10px;width:100%;height:34px}
.copyright{position:absolute;left:70px;top:296px;font-size:11px;color:var(--muted);line-height:1.6}
</style>
</head>
<body>

<header class="hero">
  <div class="hero-media" role="img" aria-label="Aerial photograph of a city park surrounded by high-rise apartment towers"></div>
  <div class="hero-shade"></div>
  <div class="topbar">
    <div class="brand"><span class="brand-dot"></span>Skyward Lens Reels</div>
    <nav class="nav">
      <a class="active">HOME</a><a>ABOUT</a><a>SERVICES</a><a>OUR WORK</a><a>BLOG</a><a>CONTACT</a>
    </nav>
    <span class="btn btn-videos">
      <svg width="16" height="16" viewBox="0 0 16 16"><circle cx="8" cy="8" r="7" fill="none" stroke="#fff" stroke-width="1.5"/><path d="M6 5l5 3-5 3z" fill="#fff"/></svg>
      Click the Videos
    </span>
  </div>
  <div class="hero-copy">
    <div class="eyebrow">Welcome to</div>
    <h1>Skyward Lens Reels</h1>
    <p>Lorem ipsum dolor sit amet, consectetuer adipiscing elit, sed diam nonummy nibh euismod tincidunt ut laoreet dolore magna aliquam erat volutpat.</p>
  </div>
</header>

<section class="services">
  <h2 class="section-title">Advantage Services We Provide</h2>
  <div class="title-rule"></div>
  <div class="service-grid">
    <div class="service"><svg viewBox="0 0 62 62"><rect x="10" y="18" width="16" height="38" fill="#2aa7df"/><rect x="30" y="8" width="22" height="48" fill="#2aa7df"/><rect x="6" y="56" width="50" height="3" fill="#2b2f36"/></svg><span>Real Estate</span></div>
    <div class="service"><svg viewBox="0 0 62 62"><rect x="14" y="22" width="22" height="18" fill="#2aa7df"/><circle cx="18" cy="46" r="9" fill="#2b2f36"/><circle cx="44" cy="48" r="7" fill="#2b2f36"/><rect x="34" y="32" width="18" height="10" fill="#2aa7df"/></svg><span>Agricultural</span></div>
    <div class="service"><svg viewBox="0 0 62 62"><rect x="8" y="14" width="46" height="26" fill="#2aa7df"/><path d="M8 27h46M23 14v26M39 14v26" stroke="#fff" stroke-width="2"/><rect x="29" y="40" width="4" height="16" fill="#2b2f36"/></svg><span>Utilities</span></div>
    <div class="service"><svg viewBox="0 0 62 62"><path d="M8 26a23 14 0 0 1 46 0z" fill="#2aa7df"/><rect x="30" y="26" width="3" height="30" fill="#2b2f36"/><rect x="12" y="54" width="38" height="3" fill="#2b2f36"/></svg><span>Hospitality</span></div>
    <div class="service"><svg viewBox="0 0 62 62"><circle cx="31" cy="31" r="22" fill="none" stroke="#2aa7df" stroke-width="6"/><circle cx="31" cy="31" r="7" fill="#2b2f36"/></svg><span>Festivals</span></div>
    <div class="service"><svg viewBox="0 0 62 62"><path d="M10 12h42l-8 10H18z M18 26h26l-6 10H24z M24 40h14l-4 10h-6z" fill="#2aa7df"/></svg><span>Disaster<br>Relief</span></div>
    <div class="service"><svg viewBox="0 0 62 62"><rect x="10" y="14" width="42" height="42" fill="#2aa7df"/><path d="M31 22v18M22 31h18" stroke="#fff" stroke-width="5"/></svg><span>Hospitals</span></div>
    <div class="service"><svg viewBox="0 0 62 62"><path d="M8 32L31 12l23 20v24H8z" fill="#2aa7df"/><rect x="26" y="40" width="10" height="16" fill="#fff"/></svg><span>Retirement<br>Communities</span></div>
    <div class="service"><svg viewBox="0 0 62 62"><circle cx="31" cy="22" r="14" fill="#2aa7df"/><rect x="29" y="30" width="4" height="26" fill="#2b2f36"/><rect x="14" y="54" width="34" height="3" fill="#2b2f36"/></svg><span>Environmental</span></div>
    <div class="service"><svg viewBox="0 0 62 62"><circle cx="31" cy="31" r="24" fill="#2aa7df"/><path d="M7 31h48" stroke="#fff" stroke-width="2"/><ellipse cx="31" cy="31" rx="10" ry="24" fill="none" stroke="#fff" stroke-width="2"/><path d="M11 20h40M11 42h40" stroke="#fff" stroke-width="2"/></svg><span>International<br>Availability</span></div>
  </div>
</section>

<section class="videos">
  <div class="video-row">
    <article class="video-card">
      <div class="video-thumb thumb-city" role="img" aria-label="Aerial video still of a downtown intersection and city buildings">
        <svg class="play" width="52" height="52" viewBox="0 0 52 52"><circle cx="26" cy="26" r="25" fill="rgba(0,0,0,.45)"/><path d="M21 16l16 10-16 10z" fill="#fff"/></svg>
        <div class="controls"><svg width="10" height="10" viewBox="0 0 10 10"><path d="M1 0l8 5-8 5z" fill="#fff"/></svg><div class="bar"><i></i></div></div>
      </div>
      <h3>Real Estate</h3>
      <p>Lorem ipsum dolor sit amet, consectetuer adipiscing elit, sed diam nonummy nibh euismod tincidunt ut laoreet dolore magna aliquam erat volutpat.</p>
    </article>
    <article class="video-card">
      <div class="video-thumb thumb-farm" role="img" aria-label="Aerial video still of green farm fields">
        <svg class="play" width="52" height="52" viewBox="0 0 52 52"><circle cx="26" cy="26" r="25" fill="rgba(0,0,0,.45)"/><path d="M21 16l16 10-16 10z" fill="#fff"/></svg>
        <div class="controls"><svg width="10" height="10" viewBox="0 0 10 10"><path d="M1 0l8 5-8 5z" fill="#fff"/></svg><div class="bar"><i></i></div></div>
      </div>
      <h3>Agricultural</h3>
      <p>Lorem ipsum dolor sit amet, consectetuer adipiscing elit, sed diam nonummy nibh euismod tincidunt ut laoreet dolore magna aliquam erat volutpat.</p>
    </article>
    <article class="video-card">
      <div class="video-thumb thumb-solar" role="img" aria-label="Aerial video still of a solar farm beside hills">
        <svg class="play" width="52" height="52" viewBox="0 0 52 52"><circle cx="26" cy="26" r="25" fill="rgba(0,0,0,.45)"/><path d="M21 16l16 10-16 10z" fill="#fff"/></svg>
        <div class="controls"><svg width="10" height="10" viewBox="0 0 10 10"><path d="M1 0l8 5-8 5z" fill="#fff"/></svg><div class="bar"><i></i></div></div>
      </div>
      <h3>Utilities</h3>
      <p>Lorem ipsum dolor sit amet, consectetuer adipiscing elit, sed diam nonummy nibh euismod tincidunt ut laoreet dolore magna aliquam erat volutpat.</p>
    </article>
  </div>
  <span class="btn btn-more">More Videos</span>
</section>

<section class="blog">
  <h2>Latest Blog</h2>
  <div class="blog-row">
    <article class="post">
      <div class="post-thumb pt-1" role="img" aria-label="Aerial photo of a city skyline"></div>
      <h3>Lorem ipsum dolor sit amet</h3>
      <div class="meta">12 Jan 2017 / 0 Comments</div>
      <p>Lorem ipsum dolor sit amet, consectetuer adipiscing elit, sed diam nonummy nibh euismod tincidunt ut laoreet dolore magna aliquam erat volutpat.</p>
      <span class="more">READ MORE</span>
    </article>
    <article class="post">
      <div class="post-thumb pt-2" role="img" aria-label="Aerial photo of a solar array in a field"></div>
      <h3>Lorem ipsum dolor sit amet</h3>
      <div class="meta">08 Jan 2017 / 2 Comments</div>
      <p>Lorem ipsum dolor sit amet, consectetuer adipiscing elit, sed diam nonummy nibh euismod tincidunt ut laoreet dolore magna aliquam erat volutpat.</p>
      <span class="more">READ MORE</span>
    </article>
    <article class="post">
      <div class="post-thumb pt-3" role="img" aria-label="Aerial photo of an industrial plant"></div>
      <h3>Lorem ipsum dolor sit amet</h3>
      <div class="meta">03 Jan 2017 / 1 Comment</div>
      <p>Lorem ipsum dolor sit amet, consectetuer adipiscing elit, sed diam nonummy nibh euismod tincidunt ut laoreet dolore magna aliquam erat volutpat.</p>
      <span class="more">READ MORE</span>
    </article>
  </div>
</section>

<section class="newsletter">
  <svg width="36" height="30" viewBox="0 0 36 30"><path d="M1 13L35 1 27 29 17 19z" fill="none" stroke="#fff" stroke-width="2"/><path d="M17 19L35 1" stroke="#fff" stroke-width="2"/></svg>
  <h4>Subscribe Our Newsletter!</h4>
  <div class="nl-form">
    <span class="field">Enter Your Name</span>
    <span class="field">Enter Your Email</span>
    <span class="btn btn-sub">Subscribe</span>
  </div>
</section>

<footer class="footer">
  <div class="col-links">
    <h4>Quick Links</h4>
    <ul><li>Home</li><li>About</li><li>Services</li><li>Our Work</li><li>Blog</li><li>Contact</li></ul>
  </div>
  <div class="col-touch">
    <h4>Get in Touch</h4>
    <div class="touch-item"><svg width="16" height="20" viewBox="0 0 16 20"><path d="M8 1a7 7 0 0 1 7 7c0 5-7 11-7 11S1 13 1 8a7 7 0 0 1 7-7z" fill="#2aa7df"/><circle cx="8" cy="8" r="2.5" fill="#fff"/></svg><span>2150 Harbor View Road,<br>Lakemont, CA 90210</span></div>
    <div class="touch-item"><svg width="16" height="18" viewBox="0 0 16 18"><path d="M3 1h3l2 5-2 1.5a10 10 0 0 0 4 4L11.5 9l4.5 2v3a2 2 0 0 1-2 2C7 16 1 10 1 3a2 2 0 0 1 2-2z" fill="#2aa7df"/></svg><span>Phone:<br>(555) 014-3388</span></div>
    <div class="touch-item"><svg width="18" height="14" viewBox="0 0 18 14"><rect x="1" y="1" width="16" height="12" fill="#2aa7df"/><path d="M1 1l8 7 8-7" fill="none" stroke="#fff" stroke-width="1.5"/></svg><span>Email:<br>hello@skywardlensreels.example</span></div>
  </div>
  <div class="col-form">
    <h4>Contact Form</h4>
    <div class="hint">All fields marked with * are required</div>
    <div class="form-grid">
      <span class="field">Name</span>
      <span class="field">Email</span>
      <span class="field">Phone</span>
      <span class="field">Subject</span>
      <span class="field msg">Message</span>
    </div>
    <span class="btn btn-submit">Submit</span>
  </div>
  <div class="copyright">© 2017 Skyward Lens Reels. All Rights Reserved.<br>Terms &amp; Conditions | Privacy Policy | Terms of Use</div>
</footer>

</body>
</html>
```